Ferncrest Dental, LLC business card project

Business card to be designed with current logo.
Dental office- please keep design of card that looks clean and professional.
Please include the following info:
Ferncrest Dental, LLC
Dr. Lorna Pettigrew
2871 Marlowe Street
Bethlehem, PA 18093
610-555-0193
ferncrestdental.office@examplemail.test
Hello everyone-
Reason: Just got back from overseas- will look at all designs and provide feedback. Thank you!
Reason: Polling my friends for the final selection-
thank you to all those that participated- so many talented designers!

```html
<!DOCTYPE html>
<html lang="en">
<head>
<meta charset="utf-8">
<title>Ferncrest Dental, LLC — Business Card</title>
<link href="https://fonts.googleapis.com/css2?family=Questrial&family=Roboto+Condensed:wght@300;400&display=swap" rel="stylesheet">
<style>
  :root {
    --backdrop: #e4e4e4;
    --card: #ffffff;
    --brand-green: #6aa334;
    --name-green: #5f9a2c;
    --swoosh: #e3efc4;
    --icon-green: #bcd977;
    --brand-dot: #b5d65c;
    --info-grey: #9a9a9a;
  }
  * { margin: 0; padding: 0; box-sizing: border-box; }
  html, body {
    width: 1200px;
    height: 900px;
    overflow: hidden;
    background: var(--backdrop);
  }
  .canvas {
    position: relative;
    width: 1200px;
    height: 900px;
  }
  .business-card {
    position: absolute;
    left: 180px;
    top: 210px;
    width: 840px;
    height: 480px;
    background: var(--card);
    box-shadow: 0 2px 10px rgba(0,0,0,0.12);
    overflow: hidden;
  }
  .brand {
    position: absolute;
    left: 70px;
    top: 108px;
    display: flex;
    align-items: center;
    gap: 18px;
  }
  .brand-dot {
    width: 34px;
    height: 34px;
    border-radius: 50%;
    background: var(--brand-dot);
  }
  .brand-name {
    font-family: "Questrial", sans-serif;
    font-size: 58px;
    color: var(--brand-green);
    letter-spacing: 0.5px;
    line-height: 1;
  }
  .swoosh {
    position: absolute;
    left: 0;
    top: 0;
    width: 840px;
    height: 480px;
  }
  .doctor-name {
    position: absolute;
    left: 90px;
    top: 330px;
    font-family: "Questrial", sans-serif;
    font-size: 30px;
    color: var(--name-green);
  }
  .contact-list {
    position: absolute;
    left: 440px;
    top: 312px;
    list-style: none;
    font-family: "Roboto Condensed", sans-serif;
    font-weight: 300;
    font-size: 22px;
    color: var(--info-grey);
    line-height: 31px;
  }
  .contact-item {
    display: flex;
    align-items: flex-start;
    gap: 12px;
  }
  .contact-icon {
    flex: none;
    width: 24px;
    height: 24px;
    margin-top: 3px;
    fill: var(--icon-green);
  }
</style>
</head>
<body>
<main class="canvas">
  <section class="business-card">
    <div class="brand">
      <span class="brand-dot"></span>
      <span class="brand-name">Ferncrest Dental, LLC</span>
    </div>

    <svg class="swoosh" viewBox="0 0 840 480" aria-hidden="true">
      <path d="M40 325 Q420 178 805 268 Q420 205 40 325 Z" fill="var(--swoosh)"/>
    </svg>

    <p class="doctor-name">Dr. Lorna Pettigrew</p>

    <ul class="contact-list">
      <li class="contact-item">
        <svg class="contact-icon" viewBox="0 0 24 24" aria-hidden="true">
          <path d="M12 1.5a7.5 7.5 0 0 0-7.5 7.5c0 5.6 7.5 13.5 7.5 13.5s7.5-7.9 7.5-13.5A7.5 7.5 0 0 0 12 1.5zm0 10.3a2.8 2.8 0 1 1 0-5.6 2.8 2.8 0 0 1 0 5.6z"/>
        </svg>
        <span>2871 Marlowe Street<br>Bethlehem, PA 18093</span>
      </li>
      <li class="contact-item">
        <svg class="contact-icon" viewBox="0 0 24 24" aria-hidden="true">
          <path d="M6.6 10.8a15.1 15.1 0 0 0 6.6 6.6l2.2-2.2a1 1 0 0 1 1-.25 11.4 11.4 0 0 0 3.6.57 1 1 0 0 1 1 1V20a1 1 0 0 1-1 1A17 17 0 0 1 3 4a1 1 0 0 1 1-1h3.5a1 1 0 0 1 1 1c0 1.25.2 2.45.57 3.6a1 1 0 0 1-.25 1z"/>
        </svg>
        <span>610-555-0193</span>
      </li>
      <li class="contact-item">
        <svg class="contact-icon" viewBox="0 0 24 24" aria-hidden="true">
          <path d="M2 8l10-6 10 6v13H2zm2 1.2v.3l8 5 8-5v-.3l-8-4.9z"/>
        </svg>
        <span>ferncrestdental.office@examplemail.test</span>
      </li>
    </ul>
  </section>
</main>
</body>
</html>
```